Women's Health Company needs business card

We need a business card for a USA based women's health care company. We use digital technology to enhance therapy prescribed by clinicians for their patients

```html
<!DOCTYPE html>
<html lang="en">
<head>
<meta charset="utf-8">
<title>Velora Health – Business Card</title>
<link href="https://fonts.googleapis.com/css2?family=Montserrat:wght@400;500;700&display=swap" rel="stylesheet">
<style>
  :root {
    --backdrop: #2b2b2b;
    --card-white: #ffffff;
    --teal: #78bfbf;
    --teal-text: #5fb3b3;
    --purple: #7a3e98;
    --ink: #1f1f1f;
  }
  * { margin: 0; padding: 0; box-sizing: border-box; }
  html, body {
    width: 1200px;
    height: 1056px;
    overflow: hidden;
    background: var(--backdrop);
    font-family: "Montserrat", sans-serif;
  }
  .stage { position: relative; width: 1200px; height: 1056px; }
  .card {
    position: absolute;
    left: 256px;
    width: 692px;
    height: 398px;
    border-radius: 22px;
    overflow: hidden;
  }
  .card-front { top: 86px; background: var(--card-white); }
  .card-back { top: 544px; height: 392px; background: var(--teal); }

  .holder { position: absolute; left: 28px; top: 86px; }
  .holder-name {
    color: var(--purple);
    font-weight: 700;
    font-size: 26px;
    letter-spacing: 0.5px;
  }
  .holder-role { font-size: 17px; color: var(--ink); margin-top: 6px; }

  .brand-name {
    position: absolute;
    right: 38px;
    top: 60px;
    color: var(--teal-text);
    font-weight: 500;
    font-size: 46px;
    letter-spacing: 1px;
  }

  .contact-list {
    position: absolute;
    left: 28px;
    top: 240px;
    list-style: none;
  }
  .contact-list li {
    display: flex;
    align-items: center;
    gap: 10px;
    font-size: 17px;
    color: var(--ink);
    height: 28px;
  }
  .contact-list svg { width: 16px; height: 16px; fill: var(--purple); }

  .address {
    position: absolute;
    right: 38px;
    top: 272px;
    text-align: right;
    font-size: 16px;
    font-weight: 500;
    line-height: 26px;
    color: var(--ink);
  }

  .wave-band { position: absolute; left: 0; bottom: 0; width: 692px; height: 80px; }

  .brand-name-large {
    position: absolute;
    inset: 0;
    display: flex;
    align-items: center;
    justify-content: center;
    color: #ffffff;
    font-weight: 500;
    font-size: 84px;
    letter-spacing: 2px;
  }
</style>
</head>
<body>
<main class="stage">
  <section class="card card-front">
    <div class="holder">
      <div class="holder-name">MARISOL</div>
      <div class="holder-role">Co-Founder</div>
    </div>

    <div class="brand-name">Velora Health</div>

    <ul class="contact-list">
      <li>
        <svg viewBox="0 0 16 16" aria-hidden="true"><path d="M3.5 1.5l2.5 0 1 3.5-1.8 1.2a9 9 0 0 0 4.6 4.6L11 9l3.5 1v2.5c0 1-0.8 1.8-1.8 1.8A11.5 11.5 0 0 1 1.7 3.3c0-1 0.8-1.8 1.8-1.8z"/></svg>
        555-204-3817
      </li>
      <li>
        <svg viewBox="0 0 16 16" aria-hidden="true"><path d="M1 3h14v10H1z M2 4.2v0.6l6 4 6-4v-0.6z" fill-rule="evenodd"/></svg>
        hello@velorahealth.com
      </li>
      <li>
        <svg viewBox="0 0 16 16" aria-hidden="true"><circle cx="8" cy="8" r="7"/><path d="M1 8h14M8 1c-3 3.5-3 10.5 0 14M8 1c3 3.5 3 10.5 0 14" stroke="#fff" stroke-width="1" fill="none"/></svg>
        www.velorahealth.com
      </li>
    </ul>

    <div class="address">Harbor Point 2200 Ave<br>Lindale NW Suite 310</div>

    <svg class="wave-band" viewBox="0 0 692 80" preserveAspectRatio="none" aria-hidden="true">
      <path d="M0 42 C 220 40, 480 30, 692 4 L692 80 L0 80 Z" fill="var(--teal)"/>
      <path d="M300 34 C 450 30, 580 20, 692 2 L692 8 C 580 24, 450 34, 300 36 Z" fill="var(--purple)"/>
    </svg>
  </section>

  <section class="card card-back">
    <div class="brand-name-large">Velora Health</div>
  </section>
</main>
</body>
</html>
```